Thai Takeaway Menu Design

I need a menu re-design for a thai takeaway/restaurant in australia.

Please use content from the existing menu
http://www.forkmapple.example/u/menu/4930267?p=1

I'd like to emphasise on
1 - free delivery for order over $40
2 - gluten free and vegetatian option available on most meal (however you want to word it - not fuss)

*remove (the banner order online and save $10)

I'm happy to change the whole concept & design. I particularly like rustic, raw look more than moden ones. Does not need to be flowery or anything like current one :)

Industry/Entity Type

Restaurant

```html
<!DOCTYPE html>
<html lang="en">
<head>
<meta charset="utf-8">
<title>KHAO – Traditional Thai Cuisine Menu</title>
<link href="https://fonts.googleapis.com/css2?family=Italianno&family=Arimo:ital,wght@0,400;0,700;1,400&display=swap" rel="stylesheet">
<style>
:root{
  --wood-dark:#2a1209;
  --paper:#e8e2d0;
  --paper-shade:#d9d2bd;
  --frame:#a39d8f;
  --ink:#514b40;
  --dish:#b4441a;
  --pill:#716c62;
  --pill-text:#f1ede3;
  --badge:#f3e31c;
  --badge-rim:#d8c410;
  --badge-ink:#4a4636;
  --note:#f4eee0;
}
*{margin:0;padding:0;box-sizing:border-box}
html,body{width:1200px;height:849px;overflow:hidden;background:#111}
.menu{position:relative;width:1200px;height:849px;overflow:hidden;background:var(--wood-dark);font-family:"Arimo",Arial,sans-serif}
.backdrop{position:absolute;inset:0}
.panel{position:absolute;border:4px solid var(--frame);border-radius:18px}
.panel-title{font-family:"Italianno",cursive;font-weight:400;color:var(--ink);font-size:44px;line-height:1;position:absolute}
.dish-list{list-style:none;position:absolute;color:var(--dish);font-weight:700;font-size:14.5px;line-height:21.5px}
.dish-list .qty{color:#7b7467;font-weight:400}
.price{position:absolute;color:var(--ink);font-weight:700;font-size:29px}
.dinner{left:65px;top:205px;width:288px;height:172px}
.family{left:65px;top:392px;width:288px;height:212px}
.lunch{left:460px;top:230px;width:286px;height:258px}
.lunch .dish-list{text-align:center;width:100%;left:0;top:70px;line-height:24px}
.brand-box{left:836px;top:242px;width:318px;height:182px}
.brand-name{position:absolute;left:0;right:0;top:22px;text-align:center;font-family:"Italianno",cursive;font-weight:400;font-size:92px;color:#6e695e;letter-spacing:1px;line-height:1}
.brand-tag{position:absolute;left:0;right:0;top:132px;text-align:center;font-family:"Italianno",cursive;font-size:30px;color:#6e695e}
.services{position:absolute;left:872px;top:445px;font-size:17px;color:var(--ink)}
.contact{position:absolute;left:862px;top:482px;width:272px;height:94px;border-radius:16px;background:var(--pill);color:var(--pill-text);text-align:center;padding-top:14px;font-style:normal}
.contact .street{font-size:16px}
.contact .corner{font-size:12px;font-style:italic;opacity:.85;margin-top:2px}
.contact .phone{font-size:18px;font-weight:700;margin-top:4px}
.hours{position:absolute;left:460px;top:540px;width:300px;text-align:center;color:var(--ink);font-weight:700}
.hours h3{font-size:19px;margin-bottom:4px}
.hours p{font-size:14px;line-height:21px}
.badge{position:absolute;border-radius:50%;background:var(--badge);border:4px solid var(--badge-rim);box-shadow:0 3px 6px rgba(0,0,0,.35);color:var(--badge-ink);text-align:center;font-weight:700}
.badge-drink{left:456px;top:424px;width:104px;height:104px;padding-top:20px}
.badge-drink strong{display:block;font-size:19px;line-height:18px}
.badge-drink span{display:block;font-size:10.5px;line-height:11px;font-weight:400}
.badge-delivery{left:858px;top:608px;width:122px;height:122px;padding-top:24px}
.badge-delivery strong{display:block;font-size:23px;line-height:22px}
.badge-delivery span{display:block;font-size:13px;line-height:14px;font-weight:400}
.badge-delivery em{display:block;font-style:normal;font-size:30px;line-height:30px}
.dietary-note{position:absolute;left:0;top:0;pointer-events:none}
.dietary-note text{font-family:"Arimo",Arial,sans-serif;font-size:9.5px;fill:var(--note)}
</style>
</head>
<body>
<main class="menu">
  <svg class="backdrop" width="1200" height="849" viewBox="0 0 1200 849">
    <defs>
      <linearGradient id="woodTone" x1="0" y1="0" x2="1" y2="0">
        <stop offset="0" stop-color="#3a190b"/><stop offset=".5" stop-color="#62301a"/><stop offset="1" stop-color="#3a190b"/>
      </linearGradient>
    </defs>
    <rect width="1200" height="849" fill="url(#woodTone)" role="img" aria-label="Dark wooden table top"/>
    <rect x="0" y="0" width="1200" height="26" fill="#0d0d0d"/>
    <rect x="0" y="824" width="1200" height="25" fill="#0d0d0d"/>
    <g role="img" aria-label="Bowls of spices, pepper, mortar and pestle and shredded papaya across the top">
      <ellipse cx="20" cy="60" rx="40" ry="55" fill="#d7b13a"/>
      <ellipse cx="125" cy="62" rx="60" ry="45" fill="#5b3b22"/>
      <ellipse cx="290" cy="55" rx="62" ry="45" fill="#9a6a4a"/>
      <ellipse cx="490" cy="55" rx="70" ry="42" fill="#4b4741"/>
      <ellipse cx="692" cy="78" rx="70" ry="70" fill="#c7d9a0"/>
      <ellipse cx="1065" cy="90" rx="105" ry="75" fill="#3e2a1c"/>
      <ellipse cx="20" cy="250" rx="40" ry="70" fill="#3a2618"/>
    </g>
    <g role="img" aria-label="Purple orchids and orange flowers">
      <ellipse cx="840" cy="190" rx="70" ry="55" fill="#a64fc4"/>
      <ellipse cx="1180" cy="70" rx="40" ry="45" fill="#a64fc4"/>
      <ellipse cx="110" cy="650" rx="60" ry="42" fill="#a64fc4"/>
      <ellipse cx="65" cy="150" rx="45" ry="40" fill="#d9552a"/>
      <ellipse cx="1180" cy="450" rx="30" ry="45" fill="#e46a1e"/>
      <ellipse cx="1165" cy="350" rx="40" ry="50" fill="#2f6b1e"/>
    </g>
    <path d="M0 200 L60 190 140 205 230 180 330 196 420 175 520 190 620 170 720 188 820 172 920 195 1020 178 1110 196 1200 185 L1200 620 1130 640 1040 612 940 640 840 615 740 645 640 622 540 650 440 628 340 655 240 630 140 658 60 635 0 650 Z" fill="var(--paper)"/>
    <path d="M0 200 L60 190 140 205 230 180 330 196 420 175 520 190 620 170 720 188 820 172 920 195 1020 178 1110 196 1200 185" fill="none" stroke="var(--paper-shade)" stroke-width="6"/>
    <g role="img" aria-label="Bowls of cardamom, red chillies on banana leaf, dipping sauce, limes, coconut, marigolds and prawns along the bottom">
      <ellipse cx="60" cy="740" rx="95" ry="80" fill="#3a2416"/>
      <circle cx="80" cy="730" r="28" fill="#8cc23a"/>
      <circle cx="50" cy="785" r="28" fill="#8cc23a"/>
      <ellipse cx="270" cy="770" rx="100" ry="70" fill="#e9a21e"/>
      <ellipse cx="415" cy="678" rx="60" ry="55" fill="#d9621f"/>
      <ellipse cx="650" cy="745" rx="180" ry="90" fill="#5d9b2b"/>
      <ellipse cx="560" cy="720" rx="75" ry="70" fill="#c8241a"/>
      <ellipse cx="720" cy="725" rx="75" ry="75" fill="#d9a247"/>
      <ellipse cx="1120" cy="720" rx="110" ry="100" fill="#e88a5a"/>
      <ellipse cx="1150" cy="610" rx="60" ry="40" fill="#6a3426"/>
    </g>
  </svg>

  <section class="panel dinner">
    <h2 class="panel-title" style="left:26px;top:18px">Dinner for 2</h2>
    <ul class="dish-list" style="left:28px;top:60px">
      <li>Spring Rolls* <span class="qty">(4)</span></li>
      <li>Chicken &amp; Cashew Nuts</li>
      <li>Beef Massaman Curry</li>
      <li>Rice</li>
    </ul>
    <span class="price" style="left:198px;top:116px">$32</span>
  </section>

  <section class="panel family">
    <h2 class="panel-title" style="left:26px;top:18px">Family Pack</h2>
    <ul class="dish-list" style="left:28px;top:60px">
      <li>Spring Rolls* <span class="qty">(4)</span></li>
      <li>Satay Chicken Skewers <span class="qty">(4)</span></li>
      <li>Chicken &amp; Cashew Nuts</li>
      <li>Red Curry Beef</li>
      <li>Pad Thai</li>
      <li>Rice <span class="qty">(L)</span></li>
    </ul>
    <span class="price" style="left:192px;top:154px">$50</span>
  </section>

  <section class="panel lunch">
    <h2 class="panel-title" style="left:0;right:0;top:20px;text-align:center">Lunch Special</h2>
    <ul class="dish-list">
      <li>Pad Thai (Chicken &amp; Prawn)</li>
      <li>Chicken &amp; Cashew Nuts w/ Rice</li>
      <li>Beef Noodle Soup</li>
      <li>Green Curry Chicken</li>
      <li>Garlic Seafood &amp; Veg w/ Rice</li>
    </ul>
    <span class="price" style="left:102px;top:192px;font-size:40px">$12</span>
  </section>

  <div class="badge badge-drink"><strong>FREE</strong><span>Homemade<br>Pandan Drink<br>or Lemon<br>Iced Tea</span></div>

  <section class="hours">
    <h3>Trading Hours:</h3>
    <p>Lunch (Weds - Sun): 11.00 - 2.30pm</p>
    <p>Dinner (7 days): 5.00 - 9.30pm</p>
  </section>

  <header class="panel brand-box">
    <h1 class="brand-name">KHAO</h1>
    <p class="brand-tag">Traditional Thai Cuisine</p>
  </header>

  <p class="services">Dine In, Takeaway &amp; Delivery</p>
  <address class="contact">
    <div class="street">27 Larkspur Road, Eastvale</div>
    <div class="corner">(Corner of Wren St. and Larkspur Rd)</div>
    <div class="phone">Phone: 07 3000 4815</div>
  </address>

  <div class="badge badge-delivery"><strong>FREE</strong><span>delivery for<br>order over</span><em>$40</em></div>

  <svg class="dietary-note" width="1200" height="849" viewBox="0 0 1200 849">
    <path id="noteArc" d="M836 650 A86 86 0 1 0 1004 650" fill="none"/>
    <text><textPath href="#noteArc" startOffset="50%" text-anchor="middle">Meals available as gluten free or vegetarian upon request</textPath></text>
  </svg>
</main>
</body>
</html>
```